Modern Label for cleaning products for the brand Voralux

We need a label design for our line of cleaning products. The label should feature our logo and an image to identify the product's intended use. I've added our logo and an image for use. This only concerns the design of the label on the front of the bottle.

Label dimensions:
Label 1 (500ml bottle with spray): width 58mm x height 115mm
Label 2: (1L bottle): width 73mm x height 140mm
The design must be consistent for both bottles which you find in the pictures.

The bottles to be labeled are white. See the attachment for a photo of the bottles.

The photo must also appear on the label to identify the product's intended use.

Product information:
Brand: Voralux
Product: Sanitary Cleaner

This text must be placed on the label:
"Cleans, descales & freshens. followed with this text: "Ideal for quick and powerful cleaning. A ready-to-use product for everyday use."

- Mention the seperate USP's: Sanitary, Bathroom, Toilet, Wet areas

Appearance: This is a consumer product, but it must have a professional appearance. We would like to see a design that use the color blue from our logo.

Target Market(s)

Consumers who take care of their homes and want to maintain it the correct (professional) way

Font styles to use
Sans Serif

Colors
0054AA
0677BA
7BADD7
CADEEF
E8F1F8

Requirements
Must have
• USP's + use of image and logo + blend in 1 design
Nice to have
• Keep the color of the logo in the design
Should not have
• Comic sans

```html
<!DOCTYPE html>
<html lang="en">
<head>
<meta charset="utf-8">
<title>Voralux Sanitary Cleaner – Front Label</title>
<link href="https://fonts.googleapis.com/css2?family=Roboto:wght@400;500;700&family=Montserrat:wght@500;600;700&display=swap" rel="stylesheet">
<style>
  :root {
    --brand-blue: #0054AA;
    --mid-blue: #0677BA;
    --soft-blue: #7BADD7;
    --pale-blue: #CADEEF;
    --mist-blue: #E8F1F8;
    --navy: #1E2E7A;
    --ink: #1A1A1A;
    --white: #FFFFFF;
    --frame: #D6D9DE;
  }
  html, body {
    margin: 0;
    padding: 0;
    width: 1200px;
    height: 900px;
    overflow: hidden;
    background: #F3F4F6;
  }
  .canvas {
    position: relative;
    width: 1200px;
    height: 900px;
  }
  .label {
    position: absolute;
    left: 383px;
    top: 20px;
    width: 480px;
    height: 950px;
    transform: scale(0.905);
    transform-origin: top left;
    background: var(--white);
    border: 1px solid var(--frame);
    border-radius: 60px 60px 0 0;
    overflow: hidden;
    font-family: "Roboto", Arial, sans-serif;
  }
  .brand {
    position: absolute;
    left: 0;
    top: 55px;
    width: 480px;
    text-align: center;
  }
  .brand-dot {
    display: block;
    width: 88px;
    height: 88px;
    margin: 0 auto 10px;
    border-radius: 50%;
    background: var(--brand-blue);
  }
  .brand-name {
    font-family: "Montserrat", sans-serif;
    font-weight: 700;
    font-size: 44px;
    line-height: 1;
    color: var(--ink);
    letter-spacing: 0.5px;
  }
  .label-art {
    position: absolute;
    left: 0;
    top: 0;
  }
  .product-title {
    position: absolute;
    left: 0;
    top: 555px;
    width: 390px;
    height: 64px;
    background: var(--brand-blue);
    border-radius: 0 32px 32px 0;
    color: var(--white);
    font-size: 44px;
    line-height: 64px;
    padding-left: 26px;
    box-sizing: border-box;
  }
  .claim {
    position: absolute;
    left: 37px;
    top: 636px;
    margin: 0;
    font-size: 34px;
    font-weight: 700;
    line-height: 35px;
    color: var(--brand-blue);
  }
  .description {
    position: absolute;
    left: 37px;
    top: 715px;
    margin: 0;
    font-size: 16px;
    line-height: 19px;
    color: var(--brand-blue);
  }
  .divider {
    position: absolute;
    left: 37px;
    top: 767px;
    width: 296px;
    height: 2px;
    background: var(--brand-blue);
  }
  .usp-tag {
    position: absolute;
    left: 35px;
    top: 784px;
    width: 165px;
    height: 44px;
    background: var(--soft-blue);
    color: var(--white);
    font-family: "Montserrat", sans-serif;
    font-weight: 600;
    font-size: 14px;
    letter-spacing: 1px;
    line-height: 44px;
    text-align: center;
  }
  .usp-list {
    position: absolute;
    left: 35px;
    top: 832px;
    width: 166px;
    margin: 0;
    padding-bottom: 4px;
    border-bottom: 1.5px solid var(--brand-blue);
    font-family: "Montserrat", sans-serif;
    font-weight: 500;
    font-size: 12.5px;
    line-height: 17px;
    letter-spacing: 0.5px;
    color: var(--soft-blue);
    text-align: center;
  }
  .icon-tile {
    position: absolute;
    left: 380px;
    width: 64px;
    height: 64px;
    border-radius: 8px;
    background: var(--pale-blue);
    box-shadow: 0 0 0 1px var(--soft-blue);
  }
  .icon-tile svg { display: block; }
  .icon-spray { top: 655px; }
  .icon-bath { top: 735px; }
  .icon-drop { top: 816px; }
  .volume {
    position: absolute;
    left: 36px;
    top: 906px;
    font-family: "Montserrat", sans-serif;
    font-weight: 700;
    font-size: 20px;
    letter-spacing: 4px;
    color: var(--white);
  }
</style>
</head>
<body>
<div class="canvas">
  <div class="label">
    <div class="brand">
      <span class="brand-dot"></span>
      <div class="brand-name">voralux</div>
    </div>

    <svg class="label-art" width="480" height="950" viewBox="0 0 480 950">
      <defs>
        <linearGradient id="photoTone" x1="0" y1="0" x2="1" y2="0">
          <stop offset="0" stop-color="#F4F5F6"/>
          <stop offset="0.5" stop-color="#E4E4E2"/>
          <stop offset="1" stop-color="#9C9A97"/>
        </linearGradient>
        <linearGradient id="bandTone" x1="0" y1="0" x2="1" y2="0">
          <stop offset="0" stop-color="#0054AA"/>
          <stop offset="1" stop-color="#1E2E7A"/>
        </linearGradient>
        <linearGradient id="footTone" x1="0" y1="0" x2="1" y2="0">
          <stop offset="0" stop-color="#0054AA"/>
          <stop offset="1" stop-color="#1E2E7A"/>
        </linearGradient>
      </defs>
      <rect x="0" y="225" width="480" height="330" fill="url(#photoTone)" role="img" aria-label="Photo of a modern bathroom with bathtub, vanity and walk-in shower"/>
      <path d="M0 225 H480 V230 C300 200 140 220 60 330 C30 380 12 440 0 470 Z" fill="var(--brand-blue)"/>
      <path d="M0 470 C12 440 30 380 60 330 C80 300 100 280 120 265 C90 300 50 360 20 460 L0 555 Z" fill="var(--soft-blue)"/>
      <path d="M0 470 C12 440 30 380 60 330 C40 380 20 440 10 520 L0 555 Z" fill="var(--brand-blue)"/>
      <path d="M0 890 C200 890 380 860 480 740 V950 H0 Z" fill="var(--soft-blue)"/>
      <path d="M0 890 C220 888 400 850 480 770 V950 H0 Z" fill="url(#footTone)"/>
    </svg>

    <div class="product-title">Sanitary Cleaner</div>
    <h2 class="claim">Cleans Descales<br>&amp; Freshens</h2>
    <p class="description">Ideal for quick and powerful cleaning.<br>A ready-to-use product for everyday use.</p>
    <div class="divider"></div>
    <div class="usp-tag">MENTION USP'S</div>
    <p class="usp-list">SANITARY, BATHROOM,<br>TOILET, WET AREAS</p>

    <div class="icon-tile icon-spray">
      <svg width="64" height="64" viewBox="0 0 64 64" aria-label="Spray bottle">
        <path d="M22 20 H34 L38 24 H30 V28 H26 V24 H22 Z" fill="var(--brand-blue)"/>
        <path d="M24 30 H34 C36 30 38 33 38 36 V48 H20 V36 C20 33 22 30 24 30 Z" fill="var(--brand-blue)"/>
        <circle cx="44" cy="20" r="1.6" fill="var(--brand-blue)"/>
        <circle cx="48" cy="24" r="1.6" fill="var(--brand-blue)"/>
        <circle cx="44" cy="28" r="1.6" fill="var(--brand-blue)"/>
        <path d="M46 34 l1.5 3.5 3.5 1.5 -3.5 1.5 -1.5 3.5 -1.5 -3.5 -3.5 -1.5 3.5 -1.5 Z" fill="var(--brand-blue)"/>
      </svg>
    </div>
    <div class="icon-tile icon-bath">
      <svg width="64" height="64" viewBox="0 0 64 64" aria-label="Bathtub">
        <path d="M18 32 V18 C18 14 24 14 24 18" fill="none" stroke="var(--brand-blue)" stroke-width="2.5"/>
        <path d="M20 20 l4 4 M18 24 l3 4 M24 22 l3 3" stroke="var(--brand-blue)" stroke-width="1.5"/>
        <path d="M12 33 H52 V37 C52 44 46 47 40 47 H24 C18 47 12 44 12 37 Z" fill="var(--brand-blue)"/>
        <path d="M20 47 l-2 4 M44 47 l2 4" stroke="var(--brand-blue)" stroke-width="2.5"/>
        <circle cx="40" cy="28" r="3" fill="none" stroke="var(--brand-blue)" stroke-width="1.5"/>
        <circle cx="46" cy="26" r="2" fill="none" stroke="var(--brand-blue)" stroke-width="1.5"/>
      </svg>
    </div>
    <div class="icon-tile icon-drop">
      <svg width="64" height="64" viewBox="0 0 64 64" aria-label="Water drop and leaves">
        <path d="M38 14 C44 24 50 30 50 38 A12 12 0 0 1 26 38 C26 30 32 24 38 14 Z" fill="var(--brand-blue)"/>
        <path d="M14 30 C20 28 24 32 24 36 C18 38 14 34 14 30 Z" fill="var(--brand-blue)"/>
        <path d="M16 42 C22 38 26 42 26 46 C20 48 16 46 16 42 Z" fill="var(--brand-blue)"/>
        <path d="M20 22 C24 20 28 24 27 28 C23 28 20 26 20 22 Z" fill="var(--brand-blue)"/>
      </svg>
    </div>

    <div class="volume">1 LITER</div>
  </div>
</div>
</body>
</html>
```